Math Help Website Needs New Design

Looking to refresh the design of my existing site (brightsumguide.net) to be easier on the eyes. I am fully capable of doing the HTML coding and have for years, but I don't have the eye for good design, colors, layout, and fonts. This is where I need help!

I need both a new design scheme and a new logo that matches. The overall functionality will be the same as the existing site, and should not be unrecognizable.

Target Market(s)

It should appeal to students (age 13-22) and their parents, so it should NOT be childish in appearance, nor should it be corporate.

Requirements
Must have
• Should be simple, easy-to-navigate, and neither childish nor corporate. I am looking for a design for both the homepage and a similar "content" page. Simple, bold colors are preferred. A logo should be prominent at the top, with a search bar nearby. Below that I need a similar navigational area like I already have. Then, I need about 200px wide ad space on the left of the main body area.

```html
<!DOCTYPE html>
<html lang="en">
<head>
<meta charset="utf-8">
<title>Bright Sum Guide</title>
<link href="https://fonts.googleapis.com/css2?family=Ubuntu:wght@400;500;700&family=Open+Sans:ital,wght@0,400;0,600;1,400&family=Noto+Serif&display=swap" rel="stylesheet">
<style>
:root{
  --blue:#1d8ee0;
  --blue-dark:#1677c7;
  --blue-light:#3ea6ee;
  --link:#0b7fd3;
  --page:#efefef;
  --panel:#ffffff;
  --line:#dedede;
  --soft:#f1f1f1;
  --text:#333333;
  --muted:#777777;
  --green:#5aa83a;
}
*{box-sizing:border-box;margin:0;padding:0}
html,body{width:1121px;height:1200px;overflow:hidden;background:var(--page)}
body{font-family:"Open Sans",sans-serif;color:var(--text)}
.stage{position:relative;width:1300px;height:1392px;transform:scale(0.8623);transform-origin:0 0}
.abs{position:absolute}
a{color:var(--link)}
.logo{left:178px;top:22px;font-family:"Ubuntu",sans-serif;font-weight:700;font-size:33px;color:var(--blue)}
.search{left:840px;top:26px;width:298px;height:36px;display:flex}
.search-input{flex:1;border:1px solid var(--line);border-right:0;background:#fff;border-radius:4px 0 0 4px;font-size:12px;font-weight:600;color:#666;padding:10px}
.search-btn{width:88px;background:var(--blue);color:#fff;font-family:"Ubuntu",sans-serif;font-weight:500;font-size:14px;display:flex;align-items:center;justify-content:center;border-radius:0 4px 4px 0}
.nav{left:178px;top:88px;width:960px;height:52px;background:linear-gradient(var(--blue-light),var(--blue-dark));display:flex}
.nav-item{height:52px;display:flex;align-items:center;justify-content:center;color:#fff;font-family:"Ubuntu",sans-serif;font-weight:500;font-size:14.5px;border-right:1px solid #1469b0;text-shadow:0 1px 0 #0f5e9f}
.panel{background:var(--panel);border:1px solid var(--line)}
.main-panel{left:178px;top:151px;width:960px;height:763px}
.promo{left:199px;top:171px;width:199px;height:199px;background:linear-gradient(#1f4f8f,#7fa9d6 60%,#c7dff2)}
.welcome{left:418px;top:171px;width:701px;height:199px;background:linear-gradient(90deg,#e6e6e6,#fafafa 55%,#eeeeee)}
.welcome-art{position:absolute;left:0;top:0;width:360px;height:199px;background:radial-gradient(circle at 45% 55%,#f3d84a 0,#e55bd6 30%,#4fc04c 55%,#e8e8e8 80%)}
.welcome-text{position:absolute;left:366px;top:16px;width:325px;font-size:11px;line-height:17px}
.welcome-text h1{font-family:"Noto Serif",serif;font-weight:400;font-size:22px;margin-bottom:8px;color:#222}
.welcome-text p{margin-bottom:17px}
.disc{left:203px;top:398px;width:389px}
.section-title{font-family:"Noto Serif",serif;font-size:17px;color:#333;display:flex;align-items:center;gap:8px;margin-bottom:10px}
.disc ul{list-style:none}
.disc li{height:31px;border-bottom:1px solid #e5e5e5;font-size:11px;line-height:25px;color:#777;font-style:italic;padding-left:22px;position:relative;white-space:nowrap}
.disc li::before{content:"→";position:absolute;left:6px;font-style:normal;font-size:9px;color:#555}
.disc li a{font-style:italic}
.box-head{height:34px;background:var(--soft);border-top:1px solid #5aaee6;font-family:"Noto Serif",serif;font-size:13px;padding:8px 14px;color:#222}
.live{left:617px;top:391px;width:219px;height:490px}
.online{text-align:center;color:var(--green);font-size:13px;margin-top:12px;letter-spacing:.5px}
.can-help{text-align:center;font-size:10.5px;letter-spacing:.6px;margin-top:2px}
.live-btn{margin:10px auto 0;width:180px;height:32px;border-radius:4px;background:linear-gradient(#8ccc63,#4f9f33);border:2px solid #d7edc9;color:#fff;font-weight:600;font-size:14px;display:flex;align-items:center;justify-content:center;gap:12px}
.q{display:flex;gap:8px;padding:0 24px;margin-top:10px;font-size:10px;line-height:12px;letter-spacing:.7px}
.q .av{width:26px;height:26px;background:#9a9a9a;border-radius:3px;flex:none;margin-top:2px}
.q p{color:var(--link)}
.q span{color:#777}
.by{position:absolute;left:111px;top:474px;font-size:10px;letter-spacing:.8px;text-decoration:underline;color:var(--link)}
.side{left:864px;width:255px}
.side ul{list-style:none}
.side li{height:33px;border-bottom:1px solid #e5e5e5;font-size:11.5px;padding:10px 0 0 17px;position:relative}
.side li::before{content:"→";position:absolute;left:5px;top:10px;font-size:9px;color:#555}
.tabs{left:178px;top:931px;display:flex;gap:4px}
.tab{height:34px;background:#e6e6e6;border:1px solid #dadada;border-bottom:0;font-family:"Noto Serif",serif;font-size:12.5px;display:flex;align-items:center;padding:0 19px;color:#333}
.tab.active{background:#fff;color:var(--link);border-top:3px solid var(--blue);height:41px;margin-top:-7px}
.tool-panel{left:178px;top:965px;width:960px;height:381px}
.toolbar{left:195px;top:992px;width:923px;height:36px;display:flex;background:#e9e9e9;gap:1px}
.tool{flex:1;background:#ededed;display:flex;align-items:center;justify-content:center;font-family:"Noto Serif",serif;font-size:15px;color:#222}
.label{font-family:"Noto Serif",serif;font-size:15px;color:#222}
.field{background:#f4f4f4;border:1px solid #dcdcdc}
.examples{left:529px;top:1074px;width:319px;height:120px;padding:6px 6px}
.examples div{font-size:11.5px;font-weight:600;color:var(--link);text-decoration:underline;height:22px;display:flex;align-items:center;gap:6px}
.plus{width:12px;height:12px;border:1px solid #5b7fa8;font-size:10px;line-height:9px;text-align:center;text-decoration:none;color:#2a4f7a;display:inline-block;background:#eef4fb}
.sponsor{left:869px;top:1054px;width:250px;height:250px;background:linear-gradient(#c6e3f6,#a9d6f3 80%,#f28c1b 80%)}
.dark-btn{background:#2f2f2f;color:#fff;font-size:12px;font-weight:600;display:flex;align-items:center;justify-content:center}
.answer{left:476px;top:1284px;width:121px;height:41px;border-radius:4px;background:linear-gradient(var(--blue-light),var(--blue-dark));color:#fff;font-family:"Ubuntu",sans-serif;font-weight:700;font-size:20px;display:flex;align-items:center;justify-content:center;border:1px solid #1366ad}
.footer{right:180px;top:1360px;font-size:11px;color:#333}
</style>
</head>
<body>
<div class="stage">
  <div class="abs logo">Bright Sum Guide</div>
  <div class="abs search"><div class="search-input">Type your keywords...</div><div class="search-btn">SEARCH</div></div>

  <nav class="abs nav">
    <div class="nav-item" style="width:79px">HOME</div>
    <div class="nav-item" style="width:97px">ALGEBRA</div>
    <div class="nav-item" style="width:113px">GEOMETRY</div>
    <div class="nav-item" style="width:67px">TRIG</div>
    <div class="nav-item" style="width:104px">CALCULUS</div>
    <div class="nav-item" style="width:106px">STATISTICS</div>
    <div class="nav-item" style="width:159px">MORE SUBJECTS ▾</div>
    <div class="nav-item" style="width:150px">MESSAGE BOARD</div>
  </nav>

  <div class="abs panel main-panel"></div>
  <div class="abs promo" role="img" aria-label="Advertisement: apartment listing banner with a city tower"></div>
  <div class="abs welcome">
    <div class="welcome-art" role="img" aria-label="Colourful 3D math symbols: percent, plus, minus and divide"></div>
    <div class="welcome-text">
      <h1>Welcome to....</h1>
      <p>Math Lessons - Looking to understand a subject better, or maybe you don't understand what your textbook is trying to tell you? We have a collection of <a href="#">algebra</a> and <a href="#">geometry</a> lessons that you can view online right now.</p>
      <p>Ask your question on our <a href="#">math help message board</a>. Just be sure to explain what you've tried to do and where you're stuck, and a friendly volunteer may try to assist you!</p>
    </div>
  </div>

  <section class="abs disc">
    <h2 class="section-title"><svg width="15" height="12" viewBox="0 0 15 12"><ellipse cx="7.5" cy="5" rx="7" ry="4.6" fill="#1d8ee0"/><path d="M3 8 L2 12 L7 9z" fill="#1d8ee0"/></svg><span style="font-weight:400">Current Discussions</span></h2>
    <ul>
      <li><a href="#">Question relating to hcf, lcm and time...</a> Posted by: numfox21</li>
      <li><a href="#">Exponential growth question</a> Posted by: euclidian</li>
      <li><a href="#">Help!! metric units</a> Posted by: KarlT</li>
      <li><a href="#">Calculating percentile and standard d...</a> Posted by: DrNorm</li>
      <li><a href="#">Linear word problem</a> Posted by: KarlT</li>
      <li><a href="#">Ugg...</a> Posted by: MarkQR</li>
      <li><a href="#">More Arc Length</a> Posted by: MarkQR</li>
      <li><a href="#">Split - same issue, I need major help...</a> Posted by: Rosalindev</li>
      <li><a href="#">Solving for a Constant Return to arri...</a> Posted by: Rosalindev</li>
      <li><a href="#">Help with percentage question!!</a> Posted by: Arvind Mehra</li>
      <li><a href="#">Weighing puzzler</a> Posted by: KarlT</li>
      <li><a href="#">Quiz Problem I got Wrong</a> Posted by: seeitnow</li>
      <li><a href="#">Need help with this Vector problem!</a> Posted by: jkdaniel</li>
      <li><a href="#">Precalculus word problem</a> Posted by: MarkQR</li>
      <li><a href="#">Law of Sines/Cosines help.</a> Posted by: DrNorm</li>
    </ul>
  </section>

  <section class="abs live">
    <div class="box-head">Live Study Help</div>
    <div class="online">41 people online</div>
    <div class="can-help">They can help you right now!</div>
    <div class="live-btn"><svg width="12" height="12"><rect width="12" height="12" rx="2" fill="#e8f3e0"/></svg>Get Live Help</div>
    <div class="q"><div class="av"></div><p>The directions on a box of muffin mix calls for 1-2/3 cup muffin mix and 4/3 cups water. If there is only 1 cup of muffin mix left in the ...<br><span>&nbsp;0 replies</span></p></div>
    <div class="q"><div class="av"></div><p>If 3 shirts cost $90, find the cost of 4 shirts. ... <span>7 replies</span></p></div>
    <div class="q"><div class="av"></div><p>For questions 1-2, which graph represents the solution to the given system? 1. y = -x + 2 y = 3x - 1 (1 point) ... <span>1 reply</span></p></div>
    <div class="q"><div class="av"></div><p>Solve the following system using the substitution method: 6x - 2y = -4 y = 3x + 2<br><span>&nbsp;4 replies</span></p></div>
    <div class="q"><div class="av" style="background:#b89a86"></div><p>Solve the equation. 7(2b − 5) + 3 = 10 <span>5 replies</span></p></div>
    <a class="by" href="#">by StudyCircle</a>
  </section>

  <section class="abs side" style="top:391px">
    <div class="box-head">What's New?</div>
    <ul style="margin-top:6px">
      <li><a href="#">Multiplying Polynomials</a></li>
      <li><a href="#">Derivative of an Inverse Function</a></li>
      <li><a href="#">Derivatives of Logs and Exps</a></li>
      <li><a href="#">Differentiating Trig Functions</a></li>
    </ul>
  </section>
  <section class="abs side" style="top:586px">
    <div class="box-head">Math Lessons</div>
    <ul style="margin-top:6px">
      <li><a href="#">Algebra</a></li>
      <li><a href="#">Geometry</a></li>
      <li><a href="#">Trigonometry</a></li>
      <li><a href="#">Calculus</a></li>
      <li><a href="#">Statistics</a></li>
      <li><a href="#">Sports Math</a></li>
      <li><a href="#">Math Games</a></li>
      <li><a href="#">Calculators</a></li>
    </ul>
  </section>

  <div class="abs tabs">
    <div class="tab">BASIC MATH</div>
    <div class="tab">PRE-ALGEBRA</div>
    <div class="tab active">ALGEBRA</div>
    <div class="tab">TRIGONOMETRY</div>
    <div class="tab">PRECALCULUS</div>
    <div class="tab">CALCULUS</div>
    <div class="tab">STATISTICS</div>
  </div>
  <div class="abs panel tool-panel"></div>

  <div class="abs toolbar">
    <div class="tool">(▭)</div><div class="tool">[▭]</div><div class="tool">|▭|</div>
    <div class="tool"><svg width="18" height="20"><rect x="3" y="1" width="12" height="6" fill="none" stroke="#333"/><line x1="1" y1="10" x2="17" y2="10" stroke="#333"/><rect x="3" y="13" width="12" height="6" fill="none" stroke="#333"/></svg></div>
    <div class="tool">▦<sup style="font-size:8px">▫</sup></div><div class="tool">▦<sub style="font-size:8px">▫</sub></div>
    <div class="tool">√▭</div><div class="tool"><sup style="font-size:8px">▫</sup>√▭</div>
    <div class="tool">▦</div><div class="tool">(▭,▭)</div>
    <div class="tool">f(x)</div><div class="tool">ln</div><div class="tool">log</div><div class="tool">log<sub style="font-size:9px">▫</sub></div>
    <div class="tool">≥</div><div class="tool">≤</div><div class="tool">÷</div><div class="tool">π</div><div class="tool">∪</div><div class="tool">∩</div>
  </div>

  <div class="abs label" style="left:195px;top:1050px">Enter Problem: <span style="color:var(--link)">?</span></div>
  <div class="abs field" style="left:195px;top:1074px;width:315px;height:120px"></div>
  <div class="abs label" style="left:529px;top:1050px">Examples:</div>
  <div class="abs field examples">
    <div><span class="plus">+</span>Algebra Concepts and Expressions</div>
    <div><span class="plus">+</span>Points, Lines, and Line Segments</div>
    <div><span class="plus">+</span>Simplifying Polynomials</div>
    <div><span class="plus">+</span>Factoring Polynomials</div>
    <div><span class="plus">+</span>Linear Equations</div>
  </div>
  <div class="abs label" style="left:195px;top:1214px">Math Format:</div>
  <div class="abs field" style="left:195px;top:1237px;width:212px;height:27px"></div>
  <div class="abs dark-btn" style="left:407px;top:1237px;width:103px;height:27px">Show Format</div>
  <div class="abs label" style="left:529px;top:1212px">Select Topic:</div>
  <div class="abs field" style="left:529px;top:1237px;width:319px;height:27px"><svg class="abs" style="right:5px;top:6px" width="14" height="14"><rect width="14" height="14" rx="2" fill="#d6e5f6" stroke="#8fb0d6"/><path d="M4 6 L7 9 L10 6" fill="none" stroke="#3a6aa8" stroke-width="1.5"/></svg></div>
  <div class="abs answer">Answer</div>

  <div class="abs sponsor" role="img" aria-label="Advertisement: event planning service, Eventaro, eventaro.com"></div>

  <div class="abs footer">© 2012 Dana Whitlock | Sitemap</div>
</div>
</body>
</html>
```